Need a new Website Design

We are changing the project requirements because we did not get desired design. Here are the new requirements.

We sell machinery used to compact recyclable materials into neat and tidy bales. We also sell accessories and consumables related this equipment.

Our existing website is:
http://www.trenvopak.com

Our company name is 'Kelworth Trenvopak Machinery co. LTD' and we only need 1 page designed creatively. The homepage should introduce our company and what we do, as well as direct them to search or browse our balers and baler related products. It should also exude a sense of credibility, confidence and success.

Important Notes:
Links to the logo files:
- Adobe Illustrator format: http://www.trenvopak.com/assets/Trenvopak.ai
- Corel Draw format: http://www.trenvopak.com/assets/Trenvopak.cdr

Links to the Trenvopak proprietary font:
- Adobe Illustrator format: http://www.trenvopak.com/assets/Trenvopak-font.ai
- Corel Draw format: http://www.trenvopak.com/assets/Trenvopak-font.cdr

Our marketing photos can be downloaded here: http://qlinkr.example/PmQ7tR
You can see an example of the homepage on http://www.trenvopak.com/home-test/
Proprietary images are available here: http://www.snapvault.example/photos/48103977@K07/

It is important that the user should be able to access his needed baler either by type (vertical/horizontal baler) or applications straight from the homepage.

Important:
one general comment which I should have brought up from the beginning is that google analytics shows that most clients go about doing their business on our site by clicking on baler types, vertical balers, horizontal balers, and waste applications. They either want to see the whole product range first, or they already set on a manual or vertical baler, or they have no idea and thus prefer to browse the waste applications to pin down the type of waste they have have that needs to be baled. It would be good to have all of our balers and applications listed in the home page. This is one way to do it but by no means is it the right way:

http://www.trenvopak.com/home-test/

Target Market(s)

Industrial

Industry/Entity Type

Marketing

Requirements
Must have
• The logo and machine colors should be used for the color scheme. It must appeal to an international and eclectic market of recyclers, traders and small businesses. Other than that it should look and feel authentic.
Nice to have
• N/A
Should not have
• N/A

```html
<!DOCTYPE html>
<html lang="en">
<head>
<meta charset="utf-8">
<title>Trenvopak – Your Baling Solution</title>
<link href="https://fonts.googleapis.com/css2?family=Ubuntu:wght@400;500;700&display=swap" rel="stylesheet">
<style>
:root{
  --navy:#1c2a36;
  --blue-dark:#1b4a6e;
  --blue:#1f77b8;
  --blue-band:#2a7fc0;
  --lime:#b8d433;
  --lime-dark:#8fb21e;
  --green:#1d7a3a;
  --orange:#f06a14;
  --heading-blue:#1f6fae;
  --text:#3a3a3a;
  --muted:#666;
  --page:#efefef;
  --line:#d6d6d6;
}
*{box-sizing:border-box;margin:0;padding:0}
html,body{width:876px;height:1200px;overflow:hidden}
body{font-family:"Ubuntu",Arial,sans-serif;color:var(--text);background:var(--page);position:relative}
.backdrop{position:absolute;left:0;top:0;width:876px;height:376px;
  background:linear-gradient(180deg,#215a86 0%,#1a3b56 55%,#16324a 86%);}
.backdrop .white-stripe{position:absolute;left:0;top:322px;width:100%;height:6px;background:#fff}
.backdrop .blue-band{position:absolute;left:0;top:328px;width:100%;height:44px;background:var(--blue-band)}
.backdrop .lime-line{position:absolute;left:0;top:372px;width:100%;height:4px;background:var(--lime)}
.abs{position:absolute}
.topbar{left:94px;top:0;width:688px;height:70px;background:var(--navy)}
.logo{left:14px;top:18px;display:flex;align-items:center;gap:6px;color:#fff;font-size:22px;font-weight:400;letter-spacing:1px}
.logo .dot{width:12px;height:12px;border-radius:50%;background:var(--lime)}
.tagline{left:80px;top:44px;color:#c6d6a0;font-size:6px;letter-spacing:.5px}
.utility{right:84px;top:10px;font-size:8px;color:#c9d3da;display:flex;gap:6px}
.utility span+span::before{content:"|";margin-right:6px;color:#5b6a76}
.social{right:10px;top:7px;display:flex;gap:6px}
.social i{display:block;width:12px;height:12px;border-radius:50%;background:var(--lime)}
.import{right:10px;top:42px;display:flex;align-items:center;gap:8px;color:#fff;font-size:9.5px}
.import .flag{width:22px;height:22px;border-radius:50%;background:radial-gradient(circle at 40% 35%,#ff5a4a,#c30d0d)}
.nav{left:94px;top:80px;width:688px;height:32px;background:linear-gradient(#cfe45a,#a9c82b);display:flex;align-items:center;font-size:11px;color:#22310c}
.nav a{color:inherit;text-decoration:none;padding:0 8px;border-right:1px solid rgba(0,0,0,.15);line-height:12px}
.nav a.home{background:var(--navy);color:#fff;height:32px;line-height:32px;padding:0 10px;margin-left:3px;border:0}
.nav a:nth-last-of-type(1){border:0}
.search{margin-left:auto;display:flex;gap:4px;margin-right:6px}
.search .field{width:112px;height:16px;background:#fff;border:1px solid #9aab4a;font-size:7px;color:#aaa;padding:3px 6px}
.search .go{width:24px;height:16px;background:var(--blue-dark);color:#fff;font-size:7.5px;font-weight:700;text-align:center;line-height:16px}
.hero{left:94px;top:122px;width:688px;height:226px;background:linear-gradient(120deg,#1a4a36 0%,#2c8a55 35%,#3ea066 60%,#c9d6d0 100%);border-radius:3px}
.hero-caption{left:468px;top:166px;width:314px;height:98px;background:rgba(255,255,255,.85);padding:22px 0 0 16px}
.hero-caption .small{font-size:14px;font-weight:500;color:#222}
.hero-caption .small b{font-size:23px;color:var(--blue);font-weight:500}
.hero-caption .big{font-size:28px;font-weight:700;color:#111;line-height:26px;letter-spacing:.5px}
.col{top:394px;width:202px}
.col h2{font-size:17.5px;font-weight:700;padding-bottom:5px;border-bottom:1px solid var(--line)}
.col .photo{margin-top:8px;height:78px;border:4px solid #fff;box-shadow:0 0 2px #bbb}
.col h3{font-size:11px;font-weight:500;color:#111;margin-top:12px;margin-bottom:2px}
.col ul{list-style:none;font-size:8.5px;color:#444}
.col li{padding:4px 0 3px 8px;border-bottom:1px solid #e0e0e0;position:relative}
.col li::before{content:"";position:absolute;left:1px;top:7px;border-left:3px solid var(--blue);border-top:2.5px solid transparent;border-bottom:2.5px solid transparent}
.col .more{display:block;text-align:right;font-size:7px;color:var(--blue);margin-top:8px;padding-right:6px}
.divider{left:94px;top:622px;width:614px;height:1px;background:var(--line)}
.whatwedo{left:94px;top:640px;width:450px}
.whatwedo h2{font-size:23px;font-weight:700;color:var(--heading-blue);padding-bottom:4px;border-bottom:1px solid var(--line)}
.whatwedo p{font-family:Arial,sans-serif;font-size:8px;line-height:11px;color:#444;margin-top:10px}
.whatwedo .cta{font-family:"Ubuntu",sans-serif;font-size:11.5px;color:#333;margin-top:14px}
.whatwedo .cta b{color:var(--green);font-weight:500}
.btn{width:188px;height:38px;border-radius:2px;color:#fff;font-size:11.5px;font-weight:700;line-height:12px;display:flex;align-items:center;padding-left:52px;text-shadow:0 1px 1px rgba(0,0,0,.35)}
.btn.green{background:linear-gradient(#8cc63e,#5d9d24)}
.btn.blue{background:linear-gradient(#67b5e6,#2e88c6)}
.btn.orange{background:linear-gradient(#ffb640,#f08a14)}
.btn .icon{position:absolute;left:8px;top:5px;width:30px;height:30px;border-radius:4px}
.btn .ten{position:absolute;left:6px;top:0;font-size:36px;color:#111;text-shadow:none;line-height:38px;letter-spacing:-2px}
.vline{left:566px;top:672px;width:1px;height:312px;background:var(--line)}
.warranty{left:590px;top:646px;display:flex;align-items:center;gap:6px}
.warranty .badge{width:68px;height:56px;background:radial-gradient(circle,#e9383b 40%,#b8161a 70%);border-radius:50%}
.warranty span{font-size:19px;font-weight:700;color:#111}
.testi-head{left:588px;top:732px;width:178px;font-size:17.5px;font-weight:700;color:var(--heading-blue);padding-bottom:3px;border-bottom:1px solid var(--line)}
.quote{left:590px;top:766px;width:174px;height:152px;background:var(--navy);color:#fff;padding:14px 12px}
.quote h4{font-size:15px;font-weight:500;margin-bottom:8px}
.quote p{font-size:7.5px;line-height:10.5px}
.quote-tail{left:610px;top:918px}
.person{left:592px;top:946px;display:flex;gap:6px}
.person .avatar{width:44px;height:38px;background:linear-gradient(#8aa4b8,#5a7486)}
.person b{font-size:12.5px;color:#333;font-weight:700}
.person small{display:block;font-size:7.5px;color:#555;line-height:10px;font-weight:500}
.partners-head{left:94px;top:1012px;width:688px;font-size:17.5px;font-weight:700;color:#111;padding-bottom:6px;border-bottom:1px solid var(--line)}
.partners{left:94px;top:1046px;width:688px;height:86px;background:linear-gradient(#fff,#dcdcdc);border:1px solid #ccc;border-radius:3px;display:flex;justify-content:space-around;align-items:center}
.partners i{display:block;width:62px;height:50px;background:#c9c9c9;border-radius:6px}
.footer{left:94px;top:1142px;width:688px;height:58px;background:linear-gradient(#2a6f9f,#1d4f76);color:#fff;padding:14px 16px}
.footer nav{font-size:8px;font-weight:500;display:flex;gap:6px}
.footer nav span+span::before{content:"|";margin-right:6px;opacity:.5}
.footer small{display:block;font-size:7.5px;margin-top:6px;opacity:.9}
.footer .flogo{position:absolute;right:28px;top:16px;font-size:18px;color:rgba(255,255,255,.35);display:flex;align-items:center;gap:5px}
.footer .flogo i{width:10px;height:10px;border-radius:50%;background:rgba(255,255,255,.35)}
</style>
</head>
<body>
<div class="backdrop"><div class="white-stripe"></div><div class="blue-band"></div><div class="lime-line"></div></div>

<header class="abs topbar">
  <div class="abs logo"><span class="dot"></span>TRENVOPAK</div>
  <div class="abs tagline">YOUR BALING SOLUTION</div>
  <div class="abs utility"><span>TRACK YOUR ORDER</span><span>TECHNICAL SUPPORT</span><span>CONTACT US</span></div>
  <div class="abs social"><i></i><i></i><i></i></div>
  <div class="abs import"><span class="flag"></span>IMPORTING FROM CHINA AS EASY AS 123</div>
</header>

<nav class="abs nav">
  <a class="home">Home</a><a>About us</a><a>Baler Types</a><a>Applications</a><a>Baler Accessories</a><a>Testimonials</a><a>Inquire Now!</a>
  <div class="search"><div class="field">Search...</div><div class="go">GO!</div></div>
</nav>

<div class="abs hero" role="img" aria-label="Photo of a large green horizontal baling machine installed in a factory hall"></div>
<div class="abs hero-caption">
  <div class="small">WE OFFER A <b>COMPLETE RANGE</b></div>
  <div class="big">BAILING MACHINERY</div>
</div>

<section class="abs col" style="left:94px">
  <h2 style="color:var(--heading-blue)">HORIZONTAL BALERS</h2>
  <div class="photo" role="img" aria-label="Photo of a horizontal baler line with stacked bales in a workshop" style="background:linear-gradient(#e07a2a,#7d6a55 50%,#b9a98c)"></div>
  <h3>HORIZONTAL BALER SERIES</h3>
  <ul><li>Fully Automatic Horizontal Baler</li><li>Manual Tie Horizontal Baler</li><li>Top Force Auto-Tie Automatic Baler</li><li>Heavy Duty Horizontal Bagging Baler</li></ul>
  <span class="more">View All...</span>
</section>
<section class="abs col" style="left:334px">
  <h2 style="color:var(--orange)">VERTICAL BALERS</h2>
  <div class="photo" role="img" aria-label="Product shot of a blue vertical baler on white" style="background:radial-gradient(ellipse at center,#2b6fd0 0 30%,#fff 55%)"></div>
  <h3>VERTICAL BALER SERIES</h3>
  <ul><li>Standard Mill Size Baler</li><li>Lifting Chamber Baler</li><li>Long Stroke Baler</li><li>Swivel Twin Baler</li></ul>
  <span class="more">View All...</span>
</section>
<section class="abs col" style="left:574px">
  <h2 style="color:var(--green)">APPLICATIONS</h2>
  <div class="photo" role="img" aria-label="Photo of chopped straw loaded in a blue baler chamber" style="background:linear-gradient(#d8d8d8,#c2a880 55%,#2f6f9a 70%,#1f4f70)"></div>
  <ul style="margin-top:10px"><li>Aluminum Alloy Frame/Sheet</li><li>Aluminum Can Baling</li><li>Cardboard Baler (e.g. OCC, Carton)</li><li>Chopped Straw/Hay</li><li>Cotton Seed</li></ul>
  <span class="more">View All...</span>
</section>
<div class="abs divider"></div>

<section class="abs whatwedo">
  <h2>WHAT WE DO!</h2>
  <p>Trenvopak, a pioneer baler manufacturer, supplies industry-leading and cost-effective baling solutions for all types of waste material. From small standalone vertical presses to fully automated horizontal lines, we offer a complete range of baling machinery. Our smartly designed machines are CE certified, with top brand hydraulics and electric components. Durability and affordable prices make our machinery stands out among similar baling presses. As a pioneer in the waste recycling market, we help you turn your waste into a new source of profit.</p>
  <p style="margin-top:8px">Be ready to witness large savings on recycling and waste removal costs. Trenvopak waste specialists work around the hour and across the globe to bring you considerate after-sales service, strict quality standards and long term value for your most challenging waste handling projects.</p>
  <p class="cta"><b>Contact Us</b> now and our engineers will help tailor a solution, best fit to your needs.</p>
</section>

<div class="abs btn green" style="left:118px;top:838px"><span class="icon" role="img" aria-label="Support agent illustration" style="background:#d9a36a"></span>HOW CAN WE<br>HELP YOU?</div>
<div class="abs btn green" style="left:334px;top:838px"><span class="icon" role="img" aria-label="Film reel illustration" style="background:#333"></span>VIDEOS LIBRARY</div>
<div class="abs btn blue" style="left:118px;top:890px"><span class="icon" role="img" aria-label="Catalogue cover photo" style="background:#9a7a52"></span>PRODUCT<br>CATALOGUE</div>
<div class="abs btn blue" style="left:334px;top:890px"><span class="icon" style="background:#fff;border-radius:50%"></span>ON STREAMHUB</div>
<div class="abs btn orange" style="left:118px;top:942px"><span class="ten">10</span>REASONS FOR<br>CHOOSING TRENVOPAK</div>
<div class="abs btn orange" style="left:334px;top:942px"><span class="icon" role="img" aria-label="Camera and photos illustration" style="background:#e8e8e8"></span>PRODUCT GALLERY</div>

<div class="abs vline"></div>
<div class="abs warranty"><div class="badge" role="img" aria-label="Two year warranty seal"></div><span>WARRANTY</span></div>
<h2 class="abs testi-head">TESTIMONIALS</h2>
<div class="abs quote">
  <h4>Hello</h4>
  <p>We'd be happy to send our company informations to your customers so they can ask us about the press-machine. We are very happy with the pressing machine and did not meet any difficulties using it.</p>
  <p style="margin-top:10px">Please let us know if your future clients need reference, we'd be happy to help!</p>
</div>
<svg class="abs quote-tail" width="22" height="22" viewBox="0 0 22 22"><path d="M0 0H22L4 22Z" fill="var(--navy)"/></svg>
<div class="abs person">
  <div class="avatar" role="img" aria-label="Customer photo in a textile warehouse"></div>
  <div><b>Mr.Kadir</b><small>Velnor Textilhandel</small><small>Germany</small></div>
</div>

<h2 class="abs partners-head">OUR PARTNERS</h2>
<div class="abs partners"><i></i><i></i><i></i><i></i><i></i></div>

<footer class="abs footer">
  <nav><span>Home</span><span>About us</span><span>Baler Types</span><span>Applications</span><span>Baler Accessories</span><span>Terms &amp; Conditions</span></nav>
  <small>© 2013 Trenvopak Machinery Company Limited. All Rights Reserved.</small>
  <div class="flogo"><i></i>TRENVOPAK</div>
</footer>
</body>
</html>
```